Flyer for spiritual retreat (yoga, meditation, reiki, raw food)

I would like a flyer to promote my upcoming retreat and a matching Facebook banner.

The name of the retreat is "Wavecrest Of Calm" and the tagline is "retreat into you"

The activities in the retreat include daily meditation, ecstatic dance, spiritual development workshops on intuition, energy healing etc and a reiki session is included.

I would like a flyer designed to promote this, something that is editable as I will be running this multiple times and will need to adjust the flyer to add the dates etc each time.

edit: add that here will be fully catered raw food and juices, and that the retreat price includes all accomodation, meals and workshops.

Please contact me if you need further info. Please also visit my website www.marithovland.com and www.facebook.com/tolvanahaven to see my current events and promotions.

Thank you,

Marit

Reason: Hi all, thank you all for your submissions. Apologies as I am traveling and do not have much access to internet and will review your submissions and provide feedback as soon as possible. Kind regards, Marit.

Target Market(s)

People who like meditation, yoga, fans of rowan mabry and jasper vinek, those interested in personal and spiritual development.

Industry/Entity Type

Health And Wellness

Requirements
Must have
• Please put the included reiki session as as added bonus. Something like "BONUS 30 minute reiki healing session" in a little star/banner/something that stands out.
• Please emphasise the "light" part of Wavecrest as I am going for a play on words between in the light and enlightenment.
• Please include placeholder text for place, location, time
• Placeholder for price
• My name (see attached file - can change colour to suit) and website (www.marithovland.com)
Nice to have
• I prefer rounded designs, curves rather than block designs.
Should not have
• Tolvana Haven logo

```html
<!DOCTYPE html>
<html lang="en">
<head>
<meta charset="utf-8">
<title>Wavecrest Of Calm – Retreat Flyer</title>
<link href="https://fonts.googleapis.com/css2?family=Alegreya+Sans:ital,wght@0,400;0,500;0,700;0,800;1,700;1,800&family=Great+Vibes&display=swap" rel="stylesheet">
<style>
  :root {
    --stage: #2e2e30;
    --sky: #8fd1ef;
    --sky-deep: #6ec3ec;
    --mist: #e8f7fd;
    --brand-blue: #1b8fe2;
    --indigo: #3b3aa0;
    --indigo-dark: #2a2a86;
    --band-light: #4d63d4;
    --navy: #35356b;
    --ink: #2a2a5a;
    --white: #ffffff;
    --signature: #5a5a66;
  }
  * { margin: 0; padding: 0; box-sizing: border-box; }
  html, body {
    width: 1200px; height: 787px; overflow: hidden;
    background: var(--stage);
    font-family: "Alegreya Sans", sans-serif;
  }
  .flyer {
    position: absolute; left: 335px; top: 20px;
    width: 530px; height: 747px;
    background: var(--sky);
    overflow: hidden;
  }
  .flyer-art { position: absolute; inset: 0; }
  .signature {
    position: absolute; left: 288px; top: 56px; width: 240px;
    font-family: "Great Vibes", cursive; font-size: 38px; line-height: 48px;
    color: var(--signature); text-align: center; white-space: nowrap;
    transform: rotate(-6deg);
  }
  .title {
    position: absolute; left: 248px; top: 210px; width: 282px;
    text-align: center; color: var(--white); line-height: 1;
  }
  .title-line1 { display: block; height: 64px; line-height: 64px; white-space: nowrap; }
  .title-lead { font-size: 40px; font-weight: 700; }
  .title-light {
    font-size: 64px; font-weight: 800; font-style: italic;
    color: var(--brand-blue);
    text-shadow: 0 0 2px var(--white), 0 0 3px var(--white);
  }
  .title-line2 {
    display: block; font-size: 40px; font-weight: 700; font-style: italic;
    line-height: 40px;
  }
  .tagline {
    display: block; margin-top: 12px;
    font-size: 15px; font-weight: 500; letter-spacing: 1.5px;
    color: var(--ink);
  }
  .activities-heading {
    position: absolute; left: 37px; top: 399px;
    width: 164px; height: 37px; border-radius: 6px;
    background: var(--indigo); color: var(--white);
    font-size: 24px; font-weight: 700; text-align: center; line-height: 37px;
  }
  .activities {
    position: absolute; left: 44px; top: 452px; list-style: none;
    color: var(--ink); font-size: 16.5px;
  }
  .activities li {
    display: flex; align-items: center; gap: 10px; height: 27px;
  }
  .activities svg { width: 14px; height: 14px; flex: none; }
  .bonus {
    position: absolute; left: 336px; top: 358px; width: 156px; height: 156px;
  }
  .bonus svg { position: absolute; inset: 0; }
  .bonus-text {
    position: absolute; inset: 0; display: flex; flex-direction: column;
    align-items: center; justify-content: center; line-height: 1;
    color: var(--white);
  }
  .bonus-title { font-size: 20px; font-weight: 700; }
  .bonus-duration { font-size: 14px; }
  .bonus-kind { font-size: 13px; color: #6fd0ff; font-weight: 500; }
  .bonus-session { font-size: 19px; }
  .event-ribbon { position: absolute; left: 0; top: 576px; width: 530px; height: 88px; }
  .event-ribbon > svg { position: absolute; inset: 0; }
  .event-date, .event-time {
    position: absolute; top: 38px; font-size: 15px; font-weight: 700;
    color: var(--white); transform: translateX(-50%); white-space: nowrap;
  }
  .event-date { left: 183px; }
  .event-time { left: 349px; }
  .event-time em { font-style: italic; font-weight: 800; }
  .event-place {
    position: absolute; left: 265px; top: 66px; transform: translateX(-50%);
    font-size: 9.5px; color: var(--white); white-space: nowrap;
  }
  .icon { position: absolute; width: 14px; height: 14px; }
  .cost {
    position: absolute; left: 0; top: 661px; width: 530px; text-align: center;
    color: var(--ink); line-height: 1;
  }
  .cost-label { font-size: 31px; font-weight: 800; font-style: italic; }
  .cost-amount { font-size: 31px; font-weight: 800; }
  .cost-note { display: block; font-size: 9.5px; margin-top: 4px; }
  .site-bar {
    position: absolute; left: 0; bottom: 0; width: 530px; height: 34px;
    background: var(--navy); color: var(--white);
    font-size: 18px; text-align: center; line-height: 34px;
  }
  .site-bar strong { font-weight: 700; }
</style>
</head>
<body>
<main class="flyer">
  <svg class="flyer-art" viewBox="0 0 530 747" width="530" height="747">
    <defs>
      <linearGradient id="photoTone" x1="0" y1="0" x2="1" y2="1">
        <stop offset="0" stop-color="#4f8a4a"/>
        <stop offset="0.45" stop-color="#7a6a5e"/>
        <stop offset="1" stop-color="#a98d7a"/>
      </linearGradient>
      <linearGradient id="panelTone" x1="0" y1="0" x2="1" y2="0">
        <stop offset="0" stop-color="#5db6e6" stop-opacity="0.85"/>
        <stop offset="1" stop-color="#8fd1ef"/>
      </linearGradient>
      <linearGradient id="waveTone" x1="0" y1="0" x2="0" y2="1">
        <stop offset="0" stop-color="#6ec3ec"/>
        <stop offset="0.45" stop-color="#e8f7fd"/>
        <stop offset="1" stop-color="#8fd3f1"/>
      </linearGradient>
    </defs>
    <rect class="host-photo" x="0" y="0" width="320" height="400" fill="url(#photoTone)"
          role="img" aria-label="Photo of the retreat host, smiling, in a patterned top in front of garden greenery"/>
    <polygon class="title-panel" points="300,0 530,0 530,400 230,400" fill="url(#panelTone)"/>
    <path class="wave" d="M0,368 C60,330 140,318 220,332 C300,346 380,380 530,366 L530,747 L0,747 Z"
          fill="url(#waveTone)"/>
    <path class="wave-highlight" d="M0,368 C60,330 140,318 220,332 C300,346 380,380 530,366"
          fill="none" stroke="#ffffff" stroke-opacity="0.5" stroke-width="2"/>
  </svg>

  <div class="signature">Marit Hovland</div>

  <h1 class="title">
    <span class="title-line1"><span class="title-lead">Wave</span><span class="title-light">crest</span></span>
    <span class="title-line2">Of Calm</span>
    <span class="tagline">RETREAT INTO YOU</span>
  </h1>

  <div class="bonus">
    <svg viewBox="-82 -82 164 164" width="156" height="156">
      <polygon transform="rotate(7.5) scale(1.02)" fill="#6fd0ff"
        points="80,0 61.8,16.6 69.3,40 45.3,45.3 40,69.3 16.6,61.8 0,80 -16.6,61.8 -40,69.3 -45.3,45.3 -69.3,40 -61.8,16.6 -80,0 -61.8,-16.6 -69.3,-40 -45.3,-45.3 -40,-69.3 -16.6,-61.8 0,-80 16.6,-61.8 40,-69.3 45.3,-45.3 69.3,-40 61.8,-16.6"/>
      <polygon transform="scale(0.92)" fill="var(--indigo)"
        points="80,0 61.8,16.6 69.3,40 45.3,45.3 40,69.3 16.6,61.8 0,80 -16.6,61.8 -40,69.3 -45.3,45.3 -69.3,40 -61.8,16.6 -80,0 -61.8,-16.6 -69.3,-40 -45.3,-45.3 -40,-69.3 -16.6,-61.8 0,-80 16.6,-61.8 40,-69.3 45.3,-45.3 69.3,-40 61.8,-16.6"/>
    </svg>
    <div class="bonus-text">
      <span class="bonus-title">BONUS</span>
      <span class="bonus-duration">30 minute</span>
      <span class="bonus-kind">reiki healing</span>
      <span class="bonus-session">session</span>
    </div>
  </div>

  <h2 class="activities-heading">The activities</h2>
  <ul class="activities">
    <li><svg viewBox="0 0 14 14"><path d="M2 7 L6 11 L12 2" fill="none" stroke="var(--indigo)" stroke-width="2.4" stroke-linecap="round"/></svg>daily meditation,</li>
    <li><svg viewBox="0 0 14 14"><path d="M2 7 L6 11 L12 2" fill="none" stroke="var(--indigo)" stroke-width="2.4" stroke-linecap="round"/></svg>ecstatic dance,</li>
    <li><svg viewBox="0 0 14 14"><path d="M2 7 L6 11 L12 2" fill="none" stroke="var(--indigo)" stroke-width="2.4" stroke-linecap="round"/></svg>spiritual development workshops on intuition,</li>
    <li><svg viewBox="0 0 14 14"><path d="M2 7 L6 11 L12 2" fill="none" stroke="var(--indigo)" stroke-width="2.4" stroke-linecap="round"/></svg>energy healing etc</li>
  </ul>

  <div class="event-ribbon">
    <svg viewBox="0 0 530 88" width="530" height="88">
      <defs>
        <linearGradient id="bandTone" x1="0" y1="0" x2="1" y2="0">
          <stop offset="0" stop-color="var(--indigo-dark)"/>
          <stop offset="0.5" stop-color="var(--band-light)"/>
          <stop offset="1" stop-color="var(--indigo-dark)"/>
        </linearGradient>
      </defs>
      <polygon class="ribbon-tail" points="13,27 53,27 53,73 13,73 22,50" fill="var(--navy)"/>
      <polygon class="ribbon-tail" points="477,27 517,27 508,50 517,73 477,73" fill="var(--navy)"/>
      <rect class="ribbon-band" x="53" y="7" width="424" height="74" fill="url(#bandTone)"/>
    </svg>
    <svg class="icon" style="left:176px; top:20px" viewBox="0 0 14 14">
      <rect x="1.5" y="2.5" width="11" height="10" rx="1" fill="none" stroke="#fff" stroke-width="1.3"/>
      <line x1="1.5" y1="5.5" x2="12.5" y2="5.5" stroke="#fff" stroke-width="1.3"/>
      <line x1="4.5" y1="1" x2="4.5" y2="4" stroke="#fff" stroke-width="1.3"/>
      <line x1="9.5" y1="1" x2="9.5" y2="4" stroke="#fff" stroke-width="1.3"/>
    </svg>
    <svg class="icon" style="left:342px; top:20px" viewBox="0 0 14 14">
      <circle cx="7" cy="7" r="5.6" fill="none" stroke="#fff" stroke-width="1.3"/>
      <path d="M7 4 V7 L9.3 8.3" fill="none" stroke="#fff" stroke-width="1.3" stroke-linecap="round"/>
    </svg>
    <svg class="icon" style="left:259px; top:44px" viewBox="0 0 14 14">
      <path d="M7 13 C3.5 8.5 2.5 6.8 2.5 5 A4.5 4.5 0 0 1 11.5 5 C11.5 6.8 10.5 8.5 7 13 Z" fill="#fff"/>
      <circle cx="7" cy="5" r="1.7" fill="var(--band-light)"/>
    </svg>
    <span class="event-date">1st january,2017</span>
    <span class="event-time">4 pm <em>onward</em></span>
    <span class="event-place">1500s, when an unknown printer took a galley of type and scrambled it</span>
  </div>

  <p class="cost">
    <span class="cost-label">Cost</span> <span class="cost-amount">$150</span>
    <span class="cost-note">(includes all accomodation, fully catered raw food and juices, meals and workshops.)</span>
  </p>

  <footer class="site-bar">www.<strong>marithovland</strong>.com</footer>
</main>
</body>
</html>
```